christmas poster

Gift Vouchers Promotion

Buy 3 of Any Value
Get 1 More Free

The Poster Should be very modern but with a relevance to Christmas

Target Market(s)

Affluent Clients

Font styles to use
Decorative

Colors
ec1f27

Requirements
Must have
• Modern Clean Feel but Relevant to Christmas
Nice to have
• The Offer:
• Buy 3 Gift Vouchers and Receive 1 More Fee
• MUST be Big and Bold
• Include Logo

```html
<!DOCTYPE html>
<html lang="en">
<head>
<meta charset="utf-8">
<title>Holiday Special – Solenne Salon &amp; Spa</title>
<link rel="stylesheet" href="https://fonts.googleapis.com/css2?family=EB+Garamond:ital,wght@0,700;1,600;1,700&family=Great+Vibes&display=swap">
<style>
  :root {
    --brand-red: #c1202e;
    --night: #000000;
    --snow: #ffffff;
    --pine: #4a7c3a;
    --pine-deep: #3d6b30;
  }
  * { margin: 0; padding: 0; box-sizing: border-box; }
  html, body { width: 927px; height: 1200px; overflow: hidden; background: var(--snow); }
  .poster {
    position: relative;
    width: 927px;
    height: 1200px;
    background: var(--snow);
    font-family: "EB Garamond", Georgia, serif;
    overflow: hidden;
  }
  .brand {
    position: absolute;
    top: 0; left: 0;
    width: 100%;
    height: 197px;
    text-align: center;
    color: var(--brand-red);
    font-weight: 700;
  }
  .brand-name {
    display: block;
    padding-top: 38px;
    font-size: 84px;
    line-height: 1;
    letter-spacing: 1px;
  }
  .brand-line {
    display: block;
    margin-top: 14px;
    font-size: 30px;
    line-height: 1;
    letter-spacing: 14px;
  }
  .title-band {
    position: absolute;
    top: 197px; left: 0;
    width: 100%;
    height: 250px;
    background: var(--brand-red);
    display: flex;
    align-items: center;
    justify-content: center;
  }
  .title {
    font-family: "Great Vibes", cursive;
    font-weight: 400;
    color: var(--snow);
    font-size: 128px;
    line-height: 1;
    margin-top: 10px;
  }
  .offer-band {
    position: absolute;
    top: 447px; left: 0;
    width: 100%;
    height: 525px;
    background: var(--night);
    color: var(--snow);
    text-align: center;
  }
  .dots {
    position: absolute;
    left: 50%;
    transform: translateX(-50%);
    width: 110px;
    height: 16px;
  }
  .dots-top { top: 68px; }
  .dots-bottom { top: 424px; }
  .offer-line {
    position: absolute;
    left: 0; width: 100%;
    font-style: italic;
    font-weight: 700;
    line-height: 1;
  }
  .offer-buy { top: 114px; font-size: 108px; }
  .offer-free { top: 264px; font-size: 112px; letter-spacing: 1px; }
  .tree-art {
    position: absolute;
    top: 401px; left: 0;
    width: 106px;
    height: 571px;
    background: linear-gradient(180deg, var(--pine) 0%, var(--pine-deep) 100%);
  }
  .divider {
    position: absolute;
    top: 972px; left: 0;
    width: 100%;
    height: 13px;
    background: var(--snow);
  }
  .contact-band {
    position: absolute;
    top: 985px; left: 0;
    width: 100%;
    height: 215px;
    background: var(--brand-red);
    color: var(--snow);
    text-align: center;
    font-style: italic;
    font-weight: 600;
  }
  .contact-address { position: absolute; top: 66px; width: 100%; font-size: 32px; line-height: 1; }
  .contact-web { position: absolute; top: 118px; width: 100%; font-size: 31px; line-height: 1; }
</style>
</head>
<body>
<main class="poster">
  <header class="brand">
    <span class="brand-name">Solenne</span>
    <span class="brand-line">salon &amp; spa</span>
  </header>

  <section class="title-band">
    <h1 class="title">Holiday Special</h1>
  </section>

  <section class="offer-band">
    <svg class="dots dots-top" viewBox="0 0 110 16" aria-hidden="true">
      <circle cx="10" cy="8" r="7" fill="var(--snow)"/>
      <circle cx="55" cy="8" r="7" fill="var(--snow)"/>
      <circle cx="100" cy="8" r="7" fill="var(--snow)"/>
    </svg>
    <p class="offer-line offer-buy">Buy 3</p>
    <p class="offer-line offer-free">Get 1 FREE!</p>
    <svg class="dots dots-bottom" viewBox="0 0 110 16" aria-hidden="true">
      <circle cx="10" cy="8" r="7" fill="var(--snow)"/>
      <circle cx="55" cy="8" r="7" fill="var(--snow)"/>
      <circle cx="100" cy="8" r="7" fill="var(--snow)"/>
    </svg>
  </section>

  <div class="tree-art" role="img" aria-label="Stylised green Christmas tree with a white star and baubles"></div>

  <div class="divider"></div>

  <footer class="contact-band">
    <p class="contact-address">1234 Your Address Here &nbsp;|&nbsp; Your City, State 12345</p>
    <p class="contact-web">www.yourwebsiteorothercontactinfo.com</p>
  </footer>
</main>
</body>
</html>
```